Business card design for Kovantrix

I need a business card based on the logo design produced for Kovantrix. The company is focused on triathlon and endurance sport coaching and the tag line is (per the logo) "Endurance. Resilience. Achievement". The design should be sophisticated, appropriate to an affluent and business oriented target market. Colors are optional but the color of the logo probably dictates the color used on the card. I envisage using the red logo, with black print for the wording and contact numbers on a white or cream background, but am open to alternative suggestions. I expect to select something fairly conventional, but would like to see some designs that are less conventional to stretch my thinking on what could be appropriate. I am assuming a single side design is best, but willing to consider double sided as an option.

Target Market(s)

Individual athletes and corporate health and wellness leaders

Industry/Entity Type

Health And Wellness

Contact Information for Business Card

The card should provide the following information:
Logo
My name: Marcus Bellingham
Company website: Kovantrix.com
My email: marcus.bellingham@kovantrix.com
My cell phone number: +1-555-812-6093

Font styles to use
Sans Serif

Colors

Designer to choose colors to be used in the design.

Requirements
Must have
• Space on the card - simple design, not over crowded.
Nice to have
• clean and clear font, nothing garish or mass market like
Should not have
• Do not add pictures

```html
<!DOCTYPE html>
<html lang="en">
<head>
<meta charset="utf-8">
<title>Kovantrix Business Card</title>
<link rel="stylesheet" href="https://fonts.googleapis.com/css2?family=Roboto:wght@400;500;700&family=Roboto+Condensed:wght@500;700&display=swap">
<style>
  :root {
    --brand-red: #ae2629;
    --ink: #1a1a1a;
    --card-white: #f3f3f3;
    --muted: #5a5a5a;
    --backdrop: #e4e2df;
  }
  html, body {
    margin: 0;
    padding: 0;
    width: 1200px;
    height: 960px;
    overflow: hidden;
    background: var(--backdrop);
  }
  .canvas {
    position: relative;
    width: 1200px;
    height: 960px;
  }
  .card {
    position: absolute;
    width: 600px;
    height: 342px;
    border-radius: 22px;
    overflow: hidden;
    background: var(--card-white);
    box-shadow: 0 2px 6px rgba(0,0,0,0.18);
    font-family: "Roboto", sans-serif;
  }
  .card-front { left: 315px; top: 113px; }
  .card-back  { left: 311px; top: 472px; }

  .wave { position: absolute; inset: 0; width: 600px; height: 342px; }

  .brand {
    position: absolute;
    left: 33px;
    top: 66px;
  }
  .brand-name {
    margin: 0;
    font-family: "Roboto", sans-serif;
    font-weight: 700;
    font-size: 36px;
    line-height: 1;
    color: var(--brand-red);
    letter-spacing: -0.5px;
  }
  .brand-tagline {
    margin: 6px 0 0;
    font-family: "Roboto", sans-serif;
    font-weight: 500;
    font-size: 12.5px;
    color: var(--ink);
    letter-spacing: 0.2px;
  }

  .contact-list {
    position: absolute;
    left: 34px;
    top: 260px;
    margin: 0;
    padding: 0;
    list-style: none;
    color: #fff;
    font-size: 14px;
    line-height: 19.5px;
  }
  .contact-list li { display: flex; align-items: center; gap: 9px; }
  .contact-icon { width: 12px; height: 12px; flex: none; }

  .holder {
    position: absolute;
    right: 37px;
    top: 276px;
    text-align: right;
    color: #fff;
    font-family: "Roboto Condensed", sans-serif;
  }
  .holder-name { margin: 0; font-weight: 700; font-size: 21px; line-height: 1; }
  .holder-role { margin: 6px 0 0; font-weight: 500; font-size: 15px; letter-spacing: 0.5px; }

  .back-brand {
    position: absolute;
    left: 0; right: 0;
    top: 135px;
    margin: 0;
    text-align: center;
    font-weight: 700;
    font-size: 58px;
    color: var(--brand-red);
    letter-spacing: -0.5px;
  }
  .back-url {
    position: absolute;
    left: 0; right: 0;
    top: 293px;
    margin: 0;
    text-align: center;
    font-size: 14px;
    letter-spacing: 3px;
    color: var(--muted);
  }
</style>
</head>
<body>
<main class="canvas">

  <section class="card card-front" aria-label="Card front">
    <svg class="wave" viewBox="0 0 600 342" aria-hidden="true">
      <path d="M0,186 C120,152 230,160 330,196 C430,230 525,212 600,125 L600,342 L0,342 Z" fill="var(--brand-red)"/>
      <path d="M0,186 C110,146 220,146 330,186 C430,222 505,214 562,172 C500,214 425,226 330,205 C225,178 115,168 0,186 Z" fill="var(--ink)"/>
      <path d="M0,198 C150,178 300,214 420,238 C505,254 565,218 600,160" fill="none" stroke="#fff" stroke-width="2"/>
      <circle cx="450" cy="177" r="15" fill="var(--brand-red)"/>
    </svg>

    <div class="brand">
      <h1 class="brand-name">Kovantrix</h1>
      <p class="brand-tagline">ENDURANCE. RESILIENCE. ACHIEVEMENT</p>
    </div>

    <ul class="contact-list">
      <li>
        <svg class="contact-icon" viewBox="0 0 12 12" aria-hidden="true"><rect x="3" y="0.5" width="6" height="11" rx="1.2" fill="none" stroke="#fff" stroke-width="1.2"/><circle cx="6" cy="9.5" r="0.7" fill="#fff"/></svg>
        <span>+1-555-812-6093</span>
      </li>
      <li>
        <svg class="contact-icon" viewBox="0 0 12 12" aria-hidden="true"><rect x="0.5" y="2.5" width="11" height="7.5" fill="#fff"/><path d="M0.5,2.5 L6,7 L11.5,2.5" fill="none" stroke="var(--brand-red)" stroke-width="1"/></svg>
        <span>marcus.bellingham@kovantrix.com</span>
      </li>
      <li>
        <svg class="contact-icon" viewBox="0 0 12 12" aria-hidden="true"><circle cx="6" cy="6" r="5.5" fill="#fff"/><path d="M0.5,6 H11.5 M6,0.5 C3,3 3,9 6,11.5 M6,0.5 C9,3 9,9 6,11.5" fill="none" stroke="var(--brand-red)" stroke-width="0.9"/></svg>
        <span>www.Kovantrix.com</span>
      </li>
    </ul>

    <div class="holder">
      <p class="holder-name">MARCUS BELLINGHAM</p>
      <p class="holder-role">TRIATHLETE</p>
    </div>
  </section>

  <section class="card card-back" aria-label="Card back">
    <p class="back-brand">Kovantrix</p>
    <p class="back-url">www.Kovantrix.com</p>
  </section>

</main>
</body>
</html>
```